Managed Service Provider need new business cards

We are a small Maanged Service Provider of IT Services and need a new fresh design for our business cards. We want something impossible, fun and professional :)
Our services has a large range, but we are always fun and make sure our customers both get their issue sorted and also feel like they are "catching up with an old friend".
All our cards in the past has always been all black, with red and we need something fresher.
The back of card, we would like just a small list of what we do i think, but if someone has a better idea, please do something cool with the back of the card:
Managed IT Services
Productivity Solutions
Data Backup and Recovery
IT System Maintenance
Managed IT Security
More details can be found on our website tqnetworks.com.au
Industry/Entity Type
It Company
Contact Information for Business Card
Name: Dwayne Falstrup
Title: Director
Phone: 03 6193 4827
Mobile: 0412 587 239
Email: dwayne@tqnetworks.com.au
Web: www.tqnetworks.com.au

```html
<!DOCTYPE html>
<html lang="en">
<head>
<meta charset="utf-8">
<title>TQ Networks – Business Card</title>
<link rel="stylesheet" href="https://fonts.googleapis.com/css2?family=Montserrat:wght@700;800&family=Didact+Gothic&display=swap">
<style>
  :root {
    --brand-red: #e5202a;
    --brand-red-dark: #c8141d;
    --ink: #111111;
    --paper: #f6f6f6;
    --paper-shade: #e9e9ea;
    --stage: #d9dadc;
    --white: #ffffff;
  }
  * { box-sizing: border-box; margin: 0; padding: 0; }
  html, body { width: 710px; height: 1200px; overflow: hidden; }
  body {
    background: var(--stage);
    font-family: "Didact Gothic", "Century Gothic", sans-serif;
    color: var(--ink);
    position: relative;
  }
  .card {
    position: absolute;
    left: 35px;
    width: 640px;
    height: 366px;
    background: radial-gradient(circle at 70% 30%, var(--paper) 0%, var(--paper-shade) 100%);
    box-shadow: 0 6px 18px rgba(0,0,0,0.18);
    overflow: hidden;
  }
  .card--front { top: 214px; }
  .card--back { top: 620px; }

  /* Front */
  .front-panel {
    position: absolute; left: 0; top: 0; bottom: 0; width: 296px;
    background: linear-gradient(160deg, var(--brand-red) 0%, var(--brand-red-dark) 100%);
  }
  .wordmark {
    font-family: "Montserrat", sans-serif;
    font-weight: 800;
    letter-spacing: 0.5px;
    white-space: nowrap;
  }
  .front-panel .wordmark {
    position: absolute; left: 36px; top: 38px;
    font-size: 30px; color: var(--white);
  }
  .front-illustration {
    position: absolute; left: 22px; top: 172px; width: 256px; height: 128px;
    border-radius: 6px;
    background: linear-gradient(180deg, rgba(255,255,255,0.18) 0%, rgba(60,60,70,0.55) 100%);
  }
  .person-name {
    position: absolute; left: 296px; right: 0; top: 26px;
    text-align: center;
    font-family: "Montserrat", sans-serif; font-weight: 700;
    font-size: 31px;
  }
  .person-title {
    position: absolute; left: 296px; right: 0; top: 76px;
    text-align: center; font-size: 23px;
  }
  .contact-list {
    position: absolute; left: 280px; top: 152px;
    list-style: none;
  }
  .contact-item {
    display: flex; align-items: center;
    height: 46px; font-size: 20px;
  }
  .contact-icon {
    width: 30px; height: 30px; border-radius: 50%;
    background: var(--ink);
    display: flex; align-items: center; justify-content: center;
    margin-right: 12px; flex: none;
  }

  /* Back */
  .back-tab {
    position: absolute; left: 210px; top: 0; width: 226px; height: 30px;
    background: var(--brand-red);
    border-radius: 0 0 6px 6px;
  }
  .card--back .wordmark {
    position: absolute; left: 0; right: 0; top: 42px;
    text-align: center; font-size: 20px; color: var(--brand-red);
  }
  .service {
    position: absolute; width: 190px; text-align: center;
    font-size: 17px; line-height: 1.2;
  }
  .service-icon {
    width: 52px; height: 52px; border-radius: 50%;
    background: var(--ink);
    margin: 0 auto 8px;
    display: flex; align-items: center; justify-content: center;
  }
  .service--managed { left: 45px; top: 100px; }
  .service--productivity { left: 225px; top: 100px; }
  .service--backup { left: 405px; top: 100px; }
  .service--maintenance { left: 115px; top: 200px; }
  .service--security { left: 335px; top: 200px; }
  .back-web {
    position: absolute; left: 0; right: 0; top: 320px;
    text-align: center; font-size: 16px; color: var(--brand-red);
  }
</style>
</head>
<body>

<section class="card card--front" aria-label="Business card front">
  <div class="front-panel">
    <div class="wordmark">TQ NETWORKS</div>
    <div class="front-illustration" role="img" aria-label="Illustration of technicians servicing server racks"></div>
  </div>
  <h1 class="person-name">Dwayne Falstrup</h1>
  <p class="person-title">Director</p>
  <ul class="contact-list">
    <li class="contact-item">
      <span class="contact-icon"><svg width="16" height="16" viewBox="0 0 24 24"><path d="M6.6 10.8a15 15 0 0 0 6.6 6.6l2.2-2.2c.3-.3.7-.4 1-.2 1.1.4 2.3.6 3.6.6.6 0 1 .4 1 1V20c0 .6-.4 1-1 1A17 17 0 0 1 3 4c0-.6.4-1 1-1h3.5c.6 0 1 .4 1 1 0 1.3.2 2.5.6 3.6.1.3 0 .7-.2 1z" fill="#fff"/></svg></span>
      03 6193 4827
    </li>
    <li class="contact-item">
      <span class="contact-icon"><svg width="16" height="16" viewBox="0 0 24 24"><path d="M6.6 10.8a15 15 0 0 0 6.6 6.6l2.2-2.2c.3-.3.7-.4 1-.2 1.1.4 2.3.6 3.6.6.6 0 1 .4 1 1V20c0 .6-.4 1-1 1A17 17 0 0 1 3 4c0-.6.4-1 1-1h3.5c.6 0 1 .4 1 1 0 1.3.2 2.5.6 3.6.1.3 0 .7-.2 1z" fill="#fff"/></svg></span>
      0412 587 239
    </li>
    <li class="contact-item">
      <span class="contact-icon"><svg width="16" height="16" viewBox="0 0 24 24"><rect x="2" y="5" width="20" height="14" rx="1" fill="#fff"/><path d="M2 6l10 7 10-7" fill="none" stroke="#111" stroke-width="1.8"/></svg></span>
      dwayne@tqnetworks.com.au
    </li>
    <li class="contact-item">
      <span class="contact-icon"><svg width="17" height="17" viewBox="0 0 24 24" fill="none" stroke="#fff" stroke-width="1.8"><circle cx="12" cy="12" r="9"/><ellipse cx="12" cy="12" rx="4" ry="9"/><path d="M3 12h18M5 7h14M5 17h14"/></svg></span>
      www.tqnetworks.com.au
    </li>
  </ul>
</section>

<section class="card card--back" aria-label="Business card back">
  <div class="back-tab"></div>
  <div class="wordmark">TQ NETWORKS</div>

  <div class="service service--managed">
    <div class="service-icon"><svg width="28" height="28" viewBox="0 0 24 24" fill="none" stroke="#fff" stroke-width="1.5"><circle cx="12" cy="8" r="4"/><path d="M4 21c0-4.4 3.6-7 8-7s8 2.6 8 7"/></svg></div>
    Managed IT<br>Services
  </div>
  <div class="service service--productivity">
    <div class="service-icon"><svg width="28" height="28" viewBox="0 0 24 24" fill="none" stroke="#fff" stroke-width="1.5"><circle cx="12" cy="10" r="3"/><circle cx="12" cy="10" r="6" stroke-dasharray="2.5 2"/><path d="M4 20h16"/></svg></div>
    Productivity<br>Solutions
  </div>
  <div class="service service--backup">
    <div class="service-icon"><svg width="28" height="28" viewBox="0 0 24 24" fill="none" stroke="#fff" stroke-width="1.5"><rect x="5" y="3" width="14" height="5" rx="1"/><rect x="5" y="9.5" width="14" height="5" rx="1"/><rect x="5" y="16" width="14" height="5" rx="1"/></svg></div>
    Data Backup<br>&amp; Recovery
  </div>
  <div class="service service--maintenance">
    <div class="service-icon"><svg width="28" height="28" viewBox="0 0 24 24" fill="none" stroke="#fff" stroke-width="1.5"><circle cx="12" cy="12" r="3"/><path d="M12 3v3M12 18v3M3 12h3M18 12h3M5.6 5.6l2.1 2.1M16.3 16.3l2.1 2.1M5.6 18.4l2.1-2.1M16.3 7.7l2.1-2.1"/></svg></div>
    IT System Maintenance
  </div>
  <div class="service service--security">
    <div class="service-icon"><svg width="28" height="28" viewBox="0 0 24 24" fill="none" stroke="#fff" stroke-width="1.5"><path d="M12 3l7 3v5c0 5-3 8.5-7 10-4-1.5-7-5-7-10V6z"/><rect x="9" y="11" width="6" height="5" rx="0.5"/><path d="M10 11V9.5a2 2 0 0 1 4 0V11"/></svg></div>
    Managed IT Security
  </div>

  <p class="back-web">www.tqnetworks.com.au</p>
</section>

</body>
</html>
```